Business Card for a Mortgage Agent (myself)

I need a business card for my new job as Mortgage Agent. The Broker's logo is to be on the card as well as the brokerage License number. Not sure if to include a photo or not. Info to be on card.
Dante Roux
Mortgage Agent
Lic # M47105386
Cell: 905-614-2753
Email: danterouxk.ma@fennmail.com
Web: www.karlvostermortgages.com
TPW Brokerage Lic. # 73918

```html
<!DOCTYPE html>
<html lang="en">
<head>
<meta charset="utf-8">
<title>Dante Roux – Mortgage Agent</title>
<link rel="stylesheet" href="https://fonts.googleapis.com/css2?family=Montserrat:wght@500;600;700&display=swap">
<style>
  :root {
    --paper: #ffffff;
    --teal: #0e9a88;
    --ring-teal: #0aa3a8;
    --navy: #1d1a6b;
    --ink: #464646;
    --accent-tint: #bcc6fe;
  }
  html, body {
    margin: 0;
    padding: 0;
    width: 1200px;
    height: 686px;
    overflow: hidden;
    background: var(--paper);
  }
  .card {
    position: relative;
    width: 1200px;
    height: 686px;
    overflow: hidden;
    background: var(--paper);
    font-family: "Montserrat", sans-serif;
    color: var(--ink);
  }
  .hero {
    position: absolute;
    left: 0;
    top: 0;
  }
  .brand-name {
    position: absolute;
    left: 134px;
    top: 414px;
    width: 200px;
    margin: 0;
    text-align: center;
    font-size: 44px;
    font-weight: 700;
    color: var(--paper);
    line-height: 1;
  }
  .accent-area {
    position: absolute;
    background: var(--accent-tint);
    opacity: 0.55;
  }
  .accent-top {
    left: 1060px;
    top: 0;
    width: 140px;
    height: 144px;
  }
  .accent-bottom {
    left: 1118px;
    top: 599px;
    width: 82px;
    height: 87px;
  }
  .agent-name {
    position: absolute;
    left: 648px;
    top: 145px;
    margin: 0;
    font-size: 56px;
    font-weight: 700;
    color: var(--teal);
    line-height: 1;
    letter-spacing: 0.5px;
  }
  .agent-title {
    position: absolute;
    left: 650px;
    top: 207px;
    margin: 0;
    font-size: 24px;
    font-weight: 600;
    color: var(--teal);
    line-height: 1;
  }
  .contact-row {
    position: absolute;
    left: 650px;
    display: flex;
    align-items: center;
    font-size: 25px;
    font-weight: 600;
    color: var(--ink);
    line-height: 1;
  }
  .contact-icon {
    width: 46px;
    flex: none;
    margin-right: 16px;
  }
  .row-phone { top: 308px; }
  .row-email { top: 370px; }
  .row-web   { top: 427px; }
  .licence {
    position: absolute;
    left: 650px;
    margin: 0;
    font-size: 25px;
    font-weight: 600;
    color: var(--ink);
    line-height: 1;
  }
  .licence-agent { top: 495px; }
  .licence-brokerage { top: 554px; }
</style>
</head>
<body>
<div class="card">
  <svg class="hero" width="600" height="686" viewBox="0 0 600 686">
    <defs>
      <linearGradient id="ringGradient" x1="0" y1="0" x2="0" y2="1">
        <stop offset="0" stop-color="#1d1a6b"/>
        <stop offset="0.5" stop-color="#134f80"/>
        <stop offset="1" stop-color="#0aa3a8"/>
      </linearGradient>
      <linearGradient id="cityTone" x1="0" y1="0" x2="0" y2="1">
        <stop offset="0" stop-color="#a9c6d0"/>
        <stop offset="0.35" stop-color="#5f7f8b"/>
        <stop offset="1" stop-color="#2f4a55"/>
      </linearGradient>
    </defs>
    <circle cx="154" cy="343" r="436" fill="url(#ringGradient)"/>
    <circle cx="154" cy="343" r="412" fill="var(--ring-teal)"/>
    <circle cx="154" cy="343" r="399" fill="url(#cityTone)" role="img" aria-label="Photo of a city skyline with busy highway traffic"/>
  </svg>

  <p class="brand-name">TPW</p>

  <div class="accent-area accent-top" role="img" aria-label="Decorative grid of light violet squares"></div>
  <div class="accent-area accent-bottom" role="img" aria-label="Decorative grid of light violet squares"></div>

  <h1 class="agent-name">DANTE ROUX</h1>
  <p class="agent-title">Mortgage Agent</p>

  <div class="contact-row row-phone">
    <svg class="contact-icon" height="40" viewBox="0 0 46 40" aria-hidden="true">
      <path fill="var(--ink)" d="M6 2 l8 -1 l5 11 l-5 4 c3 7 7 11 13 14 l4 -5 l11 5 l-1 8 c-1 2 -3 2 -5 2 C18 38 3 23 3 6 c0 -2 1 -4 3 -4z"/>
    </svg>
    <span>905-614-2753</span>
  </div>
  <div class="contact-row row-email">
    <svg class="contact-icon" height="32" viewBox="0 0 46 32" aria-hidden="true">
      <rect x="1" y="1" width="44" height="30" fill="var(--ink)"/>
      <path d="M3 3 L23 19 L43 3 M3 29 L17 15 M43 29 L29 15" stroke="var(--paper)" stroke-width="2.5" fill="none"/>
    </svg>
    <span>danterouxk.ma@fennmail.com</span>
  </div>
  <div class="contact-row row-web">
    <svg class="contact-icon" height="42" viewBox="0 0 46 42" aria-hidden="true">
      <circle cx="21" cy="21" r="19" fill="var(--ink)"/>
      <g stroke="var(--paper)" stroke-width="3" fill="none">
        <ellipse cx="21" cy="21" rx="8" ry="19"/>
        <line x1="21" y1="2" x2="21" y2="40"/>
        <line x1="2" y1="15" x2="40" y2="15"/>
        <line x1="2" y1="27" x2="40" y2="27"/>
      </g>
    </svg>
    <span>www.karlvostermortgages.com</span>
  </div>

  <p class="licence licence-agent">Lic # M47105386</p>
  <p class="licence licence-brokerage">TPW Brokerage Lic. # 73918</p>
</div>
</body>
</html>
```